" Neste primeiro momento, prestaremos consultoria para gestão em saúde, oferecendo aos nossos clientes soluções que proporcionem maior eficiência no controle das operações de seus clientes, reduzindo a sinistralidade e também os custos nas carteiras de Planos de Saúde. Num segundo momento, a empresa agregará outros serviços ligados a gestão de riscos corporativos em geral. "

```html
<!DOCTYPE html>
<html lang="pt-BR">
<head>
<meta charset="utf-8">
<title>Norta — Folder institucional</title>
<link rel="stylesheet" href="https://fonts.googleapis.com/css2?family=Montserrat:wght@400;600;700&family=Open+Sans:wght@400;600&display=swap">
<style>
:root{
  --slate:#3b4246;
  --slate-dark:#2f3538;
  --teal:#2bb3a5;
  --teal-dark:#1f9589;
  --paper:#ffffff;
  --paper-grey:#e6e8e9;
  --ink:#4a5256;
  --muted:#8a9396;
  --stage:#eceeef;
}
*{box-sizing:border-box;margin:0;padding:0}
html,body{width:1200px;height:1200px;overflow:hidden;background:var(--stage);font-family:"Open Sans",Arial,sans-serif;color:var(--ink)}
.canvas{position:relative;width:1200px;height:1200px}
.panel{position:absolute;overflow:hidden;background:var(--paper)}
.spread-outer{position:absolute;left:80px;top:40px;width:1040px;height:540px;box-shadow:0 6px 20px rgba(0,0,0,.18)}
.spread-inner{position:absolute;left:80px;top:620px;width:1040px;height:540px;box-shadow:0 6px 20px rgba(0,0,0,.18)}
.half{position:absolute;top:0;width:520px;height:540px;overflow:hidden}
.half.left{left:0}.half.right{left:520px}
.brand{display:flex;align-items:center;gap:10px;font-family:"Montserrat",Arial,sans-serif;font-weight:700;letter-spacing:2px;text-transform:uppercase}
.brand-square{width:26px;height:26px;background:var(--teal)}
.photo{position:absolute}
/* back cover */
.back{background:linear-gradient(160deg,#fff 0%,var(--paper-grey) 60%)}
.back .brand{position:absolute;left:60px;top:90px;font-size:30px;color:var(--slate)}
.back .contact{position:absolute;left:70px;top:370px;color:#fff;font-size:12px}
.contact h3{font-family:"Montserrat",Arial,sans-serif;color:var(--teal);font-size:15px;font-weight:600;margin-bottom:16px}
.contact li{list-style:none;display:flex;align-items:flex-start;gap:10px;margin-bottom:10px;line-height:1.4}
.contact svg{flex:none;margin-top:1px}
/* front cover */
.front .brand{position:absolute;left:120px;top:340px;font-size:40px;color:#fff}
.front .tagline{position:absolute;left:0;right:0;top:420px;text-align:center;color:var(--teal);font-family:"Montserrat",Arial,sans-serif;font-weight:600;font-size:15px;line-height:1.4}
/* inside */
.inside{background:#fff}
.section-tab{display:inline-block;background:var(--teal);color:#fff;font-family:"Montserrat",Arial,sans-serif;font-weight:700;font-size:10px;letter-spacing:1px;padding:4px 10px}
.sub{font-family:"Montserrat",Arial,sans-serif;color:var(--teal);font-weight:700;font-size:13px;margin:8px 0 4px}
.body{font-size:10.5px;line-height:1.5;color:var(--ink)}
.company{position:absolute;left:40px;top:36px;width:440px}
.values{position:absolute;left:40px;top:250px;width:440px;display:grid;grid-template-columns:1fr 1fr;gap:14px 30px}
.value{display:flex;gap:10px}
.value-icon{flex:none;width:30px;height:30px;border-radius:50%;background:var(--teal)}
.value h4{font-family:"Montserrat",Arial,sans-serif;color:var(--teal);font-size:11px;letter-spacing:1px}
.services{position:absolute;left:40px;top:30px;width:440px}
.timeline{position:relative;margin-top:14px;padding-left:56px}
.timeline::before{content:"";position:absolute;left:16px;top:6px;bottom:10px;width:2px;background:var(--slate)}
.step{position:relative;margin-bottom:16px}
.step-dot{position:absolute;left:-56px;top:0;width:34px;height:34px;border-radius:50%;background:var(--slate);border:3px solid #fff;box-shadow:0 0 0 2px var(--slate)}
.step h4{font-family:"Montserrat",Arial,sans-serif;color:var(--teal);font-size:13px;font-weight:700;margin-bottom:2px}
.solutions{position:absolute;left:230px;top:330px;width:260px}
.solutions h4{font-family:"Montserrat",Arial,sans-serif;color:var(--teal);font-size:12px;margin-bottom:6px}
.solutions li{list-style:none;font-family:"Montserrat",Arial,sans-serif;font-weight:600;font-size:11px;color:var(--slate);display:flex;gap:6px;align-items:center;margin-bottom:4px}
.inside-footer-band{position:absolute;left:0;right:0;bottom:0;height:14px;background:var(--teal)}
</style>
</head>
<body>
<main class="canvas">

  <!-- Outside: back + front cover -->
  <section class="spread-outer">
    <div class="half left back">
      <div class="brand"><span class="brand-square"></span>Norta</div>
      <svg class="panel" style="left:0;top:0" width="520" height="540" viewBox="0 0 520 540" aria-hidden="true">
        <polygon points="0,320 520,230 520,540 0,540" fill="var(--slate)"/>
        <polygon points="0,300 520,210 520,226 0,316" fill="var(--teal)"/>
      </svg>
      <div class="contact">
        <h3>Fale Conosco</h3>
        <ul>
          <li><svg width="14" height="14" viewBox="0 0 14 14"><rect width="14" height="14" fill="var(--teal)"/><path d="M7 3a2.5 2.5 0 0 0-2.5 2.5C4.5 8 7 11 7 11s2.5-3 2.5-5.5A2.5 2.5 0 0 0 7 3z" fill="#fff"/></svg><span>Rua das Palmeiras, 120, 5º andar,<br>Centro, Niterói/RJ, Cep: 24020-000</span></li>
          <li><svg width="14" height="14" viewBox="0 0 14 14"><rect width="14" height="14" fill="var(--teal)"/><path d="M4 3l2 2-1 1.2a6 6 0 0 0 2.8 2.8L9 8l2 2-1 1.5C6.5 11.5 2.5 7.5 2.5 4z" fill="#fff"/></svg><span>(21) 3000-4521</span></li>
          <li><svg width="14" height="14" viewBox="0 0 14 14"><rect width="14" height="14" fill="var(--teal)"/><rect x="3" y="4" width="8" height="6" fill="none" stroke="#fff"/><path d="M3 4l4 3 4-3" fill="none" stroke="#fff"/></svg><span>contato@norta.com.br</span></li>
          <li><svg width="14" height="14" viewBox="0 0 14 14"><rect width="14" height="14" fill="var(--teal)"/></svg><span>/nortagestao</span></li>
        </ul>
      </div>
    </div>

    <div class="half right front" style="background:var(--slate)">
      <div class="photo" role="img" aria-label="Fotografia de uma médica sorridente de jaleco branco com estetoscópio, em ambiente hospitalar claro" style="left:0;top:0;width:520px;height:230px;background:linear-gradient(90deg,#dfe4e6 0%,#f4f6f7 55%,#cfd6d9 100%)"></div>
      <svg class="panel" style="left:0;top:0;background:none" width="520" height="540" viewBox="0 0 520 540" aria-hidden="true">
        <polygon points="0,226 520,226 520,244 0,262" fill="var(--teal)"/>
        <polygon points="0,262 520,244 520,252 0,270" fill="var(--slate-dark)"/>
      </svg>
      <div class="brand"><span class="brand-square"></span>Norta</div>
      <p class="tagline">Consultoria para gestão de riscos<br>empresariais e em saúde.</p>
    </div>
  </section>

  <!-- Inside spread -->
  <section class="spread-inner">
    <div class="half left inside">
      <div class="company">
        <span class="section-tab">A EMPRESA</span>
        <p class="sub">Norta Gestão em Saúde</p>
        <p class="body">Somos uma consultoria dedicada à gestão em saúde, com soluções que trazem eficiência ao controle das operações e reduzem custos nas carteiras de planos.</p>
        <p class="sub" style="margin-top:16px">NOSSA HISTÓRIA</p>
        <p class="body">Nossos sócios somam anos de experiência em operadoras de saúde, corretoras e administradoras, unindo conhecimento técnico e visão de mercado.</p>
      </div>
      <div class="values">
        <div class="value"><span class="value-icon"></span><div><h4>MISSÃO</h4><p class="body">Oferecer soluções que gerem eficiência e economia aos clientes.</p></div></div>
        <div class="value"><span class="value-icon"></span><div><h4>VALORES</h4><p class="body">Ética, transparência, compromisso e foco em resultados.</p></div></div>
        <div class="value"><span class="value-icon"></span><div><h4>VISÃO</h4><p class="body">Ser referência em gestão de riscos em saúde.</p></div></div>
      </div>
      <div class="photo" role="img" aria-label="Fotografia de mãos digitando em um notebook sobre a mesa de trabalho" style="left:0;top:370px;width:520px;height:170px;background:linear-gradient(135deg,#b9c2c6 0%,#e9eced 60%,#cdd4d7 100%)"></div>
      <div class="brand" style="position:absolute;left:150px;top:450px;font-size:28px;color:var(--slate)"><span class="brand-square"></span>Norta</div>
      <div class="inside-footer-band"></div>
    </div>

    <div class="half right inside">
      <div class="services">
        <span class="section-tab">SERVIÇOS</span>
        <div class="timeline">
          <div class="step"><span class="step-dot"></span><h4>Análise de entrada</h4><p class="body">Avaliação do perfil de saúde da população antes da contratação do plano.</p></div>
          <div class="step"><span class="step-dot"></span><h4>Controle de Utilização</h4><p class="body">Acompanhamento mensal da utilização e da sinistralidade, com relatórios claros.</p></div>
          <div class="step"><span class="step-dot"></span><h4>Gestão de Carteira</h4><p class="body">Gestão de grupos de risco e programas de prevenção para reduzir custos.</p></div>
          <div class="step"><span class="step-dot"></span><h4>Liberação de benefícios</h4><p class="body">Análise técnica de pedidos e autorizações de procedimentos.</p></div>
        </div>
      </div>
      <div class="photo" role="img" aria-label="Fotografia de aperto de mãos entre profissionais em reunião de negócios" style="left:0;top:380px;width:520px;height:160px;background:linear-gradient(120deg,#e8ebec 0%,#c3cbce 100%)"></div>
      <div class="solutions">
        <h4>Soluções voltadas para:</h4>
        <ul>
          <li><svg width="10" height="10"><rect width="10" height="10" fill="var(--teal)"/></svg>Empresas em geral</li>
          <li><svg width="10" height="10"><rect width="10" height="10" fill="var(--teal)"/></svg>Administradoras de Benefícios</li>
          <li><svg width="10" height="10"><rect width="10" height="10" fill="var(--teal)"/></svg>Operadoras de Planos de Saúde</li>
          <li><svg width="10" height="10"><rect width="10" height="10" fill="var(--teal)"/></svg>Corretoras</li>
        </ul>
      </div>
      <div class="inside-footer-band"></div>
    </div>
  </section>

</main>
</body>
</html>
```